Lanternfold Advisory Business Cards

We need a new layout for our business cards. We have a logo already. But we might be interested in only using the Lanternfold portion of the logo. It has been uploaded.

We would like cards that are not overly busy. Clean. Modern. Perhaps a gray color for one side.

On the back, we would like to have the lanternfold part of the logo and "Take the Leap, we've got you!"

Our business provides medics and safety training for corporate clients. Our website is www.lanternfoldadvisoryllc.example.

Industry/Entity Type

Business

Contact Information for Business Card

We want include name, email address, cell phone, main line number, and website URL on the front. Use the following as an example: Dana Kovrin, dana@lanternfoldadvisoryllc.example, 804.321.7788 (cell), 804.432.919, and www.lanternfoldadvisoryllc.example.

Font styles to use
Serif
Sans Serif

Requirements
Must have
• All required information. Back side logo with "Take the leap, we will catch you!"
Nice to have
• If possible, we would like to consider creating a card in a non-standard shape. Perhaps, the shape of a lanternfold. Just interested in understanding the option.

```html
<!DOCTYPE html>
<html lang="en">
<head>
<meta charset="utf-8">
<title>Lanternfold Advisory — Business Card</title>
<link rel="stylesheet" href="https://fonts.googleapis.com/css2?family=Cinzel:wght@400&family=Open+Sans:wdth,wght@75..100,400..600&display=swap">
<style>
  :root {
    --stage: #000000;
    --card-front: #ffffff;
    --card-back: #333333;
    --brand-blue: #1b4391;
    --ink: #222222;
    --slogan: #e8e6e6;
    --shade: rgba(0, 0, 0, 0.28);
  }
  * { margin: 0; padding: 0; box-sizing: border-box; }
  html, body {
    width: 1200px; height: 900px; overflow: hidden;
    background: var(--stage);
  }
  .canvas { position: relative; width: 1200px; height: 900px; }

  .card { position: absolute; top: 200px; width: 310px; height: 502px; overflow: hidden; }

  .card--front {
    left: 304px;
    background: var(--card-front);
    border-radius: 52px 0 52px 0;
  }
  .brand-mark {
    position: absolute; top: 60px; left: 135px;
    width: 40px; height: 40px; border-radius: 50%;
    background: var(--brand-blue);
  }
  .brand-name {
    position: absolute; top: 112px; left: 0; width: 310px;
    text-align: center; white-space: nowrap;
    font-family: "Cinzel", serif; font-weight: 400;
    font-size: 21px; letter-spacing: 0.2px;
    color: var(--ink);
  }
  .holder-name {
    position: absolute; top: 342px; left: 22px;
    font-family: "Open Sans", sans-serif; font-weight: 600;
    font-size: 18px; color: var(--brand-blue);
  }
  .contact-list {
    position: absolute; top: 398px; left: 22px; list-style: none;
    font-family: "Open Sans", sans-serif; font-size: 13.5px; color: var(--ink);
  }
  .contact-list li { display: flex; align-items: center; height: 21px; white-space: nowrap; }
  .contact-list svg { width: 11px; height: 11px; margin-right: 7px; fill: var(--brand-blue); flex: none; }

  .card--back {
    left: 641px;
    background: var(--card-back);
    border-radius: 52px 52px 0 52px;
  }
  .back-photo {
    position: absolute; left: 0; top: 40px; width: 280px; height: 420px;
    background:
      radial-gradient(ellipse 45% 22% at 62% 18%, var(--shade), transparent 70%),
      radial-gradient(ellipse 22% 40% at 28% 68%, var(--shade), transparent 70%);
  }
  .slogan {
    position: absolute; inset: 0;
    font-family: "Open Sans", sans-serif; font-weight: 600;
    font-stretch: 87%;
    color: var(--slogan); line-height: 1; text-transform: uppercase;
  }
  .slogan span { position: absolute; left: 86px; white-space: nowrap; }
  .s-take { top: 45px;  font-size: 60px; }
  .s-the  { top: 97px;  font-size: 73px; }
  .s-leap { top: 183px; font-size: 51px; }
  .s-weve { top: 247px; font-size: 51px; }
  .s-got  { top: 293px; font-size: 73px; }
  .s-you  { top: 367px; font-size: 62px; }
</style>
</head>
<body>
<div class="canvas">
  <section class="card card--front">
    <div class="brand-mark"></div>
    <div class="brand-name">Lanternfold Advisory</div>
    <div class="holder-name">Dana Kovrin</div>
    <ul class="contact-list">
      <li><svg viewBox="0 0 12 12"><path d="M3 0h6a1 1 0 0 1 1 1v10a1 1 0 0 1-1 1H3a1 1 0 0 1-1-1V1a1 1 0 0 1 1-1zm.5 1.5v8h5v-8z"/></svg>804.321.7788</li>
      <li><svg viewBox="0 0 12 12"><path d="M2.3 0.5l2 2.3-1 1.3c.7 1.6 2 2.9 3.6 3.6l1.3-1 2.3 2-1.2 2.3C5.2 11 1 6.8.5 2z"/></svg>804.432.919</li>
      <li><svg viewBox="0 0 12 12"><path d="M0 2h12v1.2L6 7 0 3.2zM0 4.6l6 3.8 6-3.8V10H0z"/></svg>dana@lanternfoldadvisoryllc.example</li>
      <li><svg viewBox="0 0 12 12"><circle cx="6" cy="6" r="5.5"/><path d="M3 4h3v2H4zM7 7h2v2H7z" fill="#fff"/></svg>www.lanternfoldadvisoryllc.example</li>
    </ul>
  </section>

  <section class="card card--back">
    <div class="back-photo" role="img" aria-label="Faint photograph of parachutists descending"></div>
    <h1 class="slogan">
      <span class="s-take">Take</span>
      <span class="s-the">The</span>
      <span class="s-leap">Leap.</span>
      <span class="s-weve">We've</span>
      <span class="s-got">Got</span>
      <span class="s-you">You.</span>
    </h1>
  </section>
</div>
</body>
</html>
```